Northern Guild of Acute Care Doctors Membership Poster Design

We need a poster that highlights why physicians should become a member of our association.

As the national voice of emergency medicine (EM), NGAD provides continuing medical education, advocates on behalf of emergency physicians and their patients, supports research and strengthens the EM community. In co-operation with other specialties and committees, NGAD also plays a vital role in the development of national standards and clinical guidelines.

NGAD keeps Canadian emergency physicians informed of developments in the clinical practice of EM and addresses political and societal changes, that affect the delivery of emergency health care.

Vision
Leading excellence in Emergency Medicine across Canada

Mission
NGAD champions excellence in Emergency Medicine in Canada by:

Advocating for Emergency Physicians and their patients;
Connecting Emergency Physicians;
Leading Emergency Medicine education;
Fostering research and innovation
Defining standards for quality Emergency Care
Collaborating with Emergency Care providers.

Target Market(s)

Physicians, Residents and Medical Students

Industry/Entity Type

Doctor

Font styles to use
Sans Serif

Requirements
Must have
• Why belong?
• Career Development
• Vision
• Leading excellence in Emergency Medicine across Canada
• Mission
• NGAD champions excellence in Emergency Medicine in Canada by:
• Advocating for Emergency Physicians and their patients;
• Connecting Emergency Physicians;
• Leading Emergency Medicine education;
• Fostering research and innovation
• Defining standards for quality Emergency Care
• Collaborating with Emergency Care providers.
• Financial Discounts
• Special rates at Brellwick Inns
• Discount on fares from Trelo Trains
• Discounts on home and auto insurance thought the Halvesta Group and Prudora Choice
• Special rates on medical and dental insurance through Bluefen Cover Canada
• Special rates with Kestrin Mobile or Vomba
• Discounts on tickets from Olstander Stageworks
• Discounts on tickets from Marquee Tours Nationwide
• Advocacy
• NGAD advocates on behalf of you and your patients
• We support the development of the specialty of emergency medicine for you
• Gain a larger voice representing you and your specialty
• Networking Opportunities
• Opportunity to become involved with NGAD committees and sections
• Connect with colleagues and potential mentors at events and through online discussions
• Member Types
• Physician Members
• Resident Members
• Student Members
• Associate Members
• ngad-example.ca
• Corporate colours or colours that are complimentary to our corporate colours
• Hex 0077b2
• Hex DF0631
Nice to have
• Pictures

```html
<!DOCTYPE html>
<html lang="en">
<head>
<meta charset="utf-8">
<title>NGAD – Why Belong?</title>
<link rel="stylesheet" href="https://fonts.googleapis.com/css2?family=Oswald:wght@400;500;600&family=Open+Sans:wght@400;600;700&display=swap">
<style>
  :root {
    --blue: #17679f;
    --red: #d2232f;
    --ink: #222;
    --paper: #fff;
    --backdrop: #4a4748;
  }
  * { box-sizing: border-box; margin: 0; padding: 0; }
  html, body { width: 726px; height: 1200px; overflow: hidden; }
  body { background: var(--backdrop); font-family: "Open Sans", Arial, sans-serif; color: var(--ink); }
  .poster { position: absolute; left: 70px; top: 60px; width: 586px; height: 1080px; background: var(--paper); }
  .photo { position: absolute; left: 0; width: 262px; }
  .photo--team { top: 0; height: 396px; background: linear-gradient(160deg, #e8eef2, #b9cbd8 60%, #5f86a8); }
  .photo--training { top: 588px; height: 176px; background: linear-gradient(135deg, #6d6a67, #9a4a44 55%, #c9b7a6); }
  .photo--workshop { top: 778px; height: 177px; background: linear-gradient(135deg, #8a5a3a, #c8a58a 50%, #4d4f5a); }
  .brand { position: absolute; left: 0; top: 396px; width: 262px; height: 192px; display: flex; align-items: center; justify-content: center; gap: 12px; }
  .brand__dot { width: 22px; height: 22px; border-radius: 50%; background: var(--red); }
  .brand__name { font-family: "Open Sans", sans-serif; font-weight: 700; font-size: 44px; color: var(--blue); letter-spacing: 1px; }
  .site { position: absolute; left: 0; top: 967px; width: 262px; height: 37px; background: var(--red); color: #fff; font-weight: 600; font-size: 21px; text-align: center; line-height: 37px; }
  .content { position: absolute; left: 285px; top: 0; width: 290px; }
  .title { position: absolute; top: 44px; left: 0; font-family: "Oswald", sans-serif; font-weight: 600; font-size: 48px; line-height: 1; color: var(--red); white-space: nowrap; }
  .subtitle { position: absolute; top: 110px; left: 0; font-family: "Oswald", sans-serif; font-weight: 400; font-size: 32px; line-height: 1; color: var(--blue); white-space: nowrap; }
  .section { position: absolute; left: 2px; width: 285px; }
  .pill { display: block; width: 236px; height: 22px; border-radius: 11px; background: var(--blue); color: #fff; font-weight: 700; font-size: 13px; line-height: 22px; padding-left: 26px; letter-spacing: .4px; }
  .lead { font-weight: 700; font-size: 11.5px; line-height: 16px; margin: 9px 0 0 5px; }
  .list { list-style: none; margin: 7px 0 0 2px; }
  .list li { position: relative; font-size: 11.6px; line-height: 16px; padding-left: 13px; margin-bottom: 3.2px; }
  .list--square li::before { content: ""; position: absolute; left: 0; top: 5px; width: 6px; height: 6px; background: var(--red); }
  .list--square li.list__lead { font-weight: 700; }
  .list--tick li { font-size: 12.4px; line-height: 18px; padding-left: 23px; margin-bottom: 7px; }
  .list--tick svg { position: absolute; left: 0; top: 4px; width: 14px; height: 11px; }
  .members { position: absolute; left: 0; top: 1028px; width: 586px; height: 30px; background: var(--blue); display: flex; align-items: center; justify-content: center; gap: 7px; font-family: "Oswald", sans-serif; font-weight: 500; font-size: 13px; color: #fff; white-space: nowrap; }
  .members__sep { width: 6px; height: 6px; border-radius: 50%; background: var(--paper); border: 1.5px solid var(--red); }
</style>
</head>
<body>
<svg width="0" height="0" style="position:absolute">
  <symbol id="tick" viewBox="0 0 14 11"><path d="M1 5.5 L5 9.5 L13 1" fill="none" stroke="#d2232f" stroke-width="2.6" stroke-linecap="round" stroke-linejoin="round"/></symbol>
</svg>

<main class="poster">
  <div class="photo photo--team" role="img" aria-label="Photo: emergency physicians attending to a patient on a hospital bed"></div>
  <div class="brand"><span class="brand__dot"></span><span class="brand__name">NGAD</span></div>
  <div class="photo photo--training" role="img" aria-label="Photo: training hall with simulation manikins"></div>
  <div class="photo photo--workshop" role="img" aria-label="Photo: physicians practising ultrasound at a workshop"></div>
  <div class="site">NGAD-EXAMPLE.CA</div>

  <div class="content">
    <h1 class="title">WHY BELONG?</h1>
    <h2 class="subtitle">CAREER DEVELOPMENT</h2>

    <section class="section" style="top:171px">
      <span class="pill">VISION</span>
      <p class="lead">Leading excellence in Emergency<br>Medicine across Canada</p>
    </section>

    <section class="section" style="top:244px">
      <span class="pill">MISSION</span>
      <ul class="list list--square" style="margin-top:9px">
        <li class="list__lead">NGAD champions excellence in Emergency Medicine in Canada by:</li>
        <li>Advocating for Emergency Physicians and their patients;</li>
        <li>Connecting Emergency Physicians;</li>
        <li>Leading Emergency Medicine education;</li>
        <li>Fostering research and innovation</li>
        <li>Defining standards for quality Emergency Care</li>
        <li>Collaborating with Emergency Care providers.</li>
      </ul>
    </section>

    <section class="section" style="top:461px">
      <span class="pill">FINANCIAL DISCOUNTS</span>
      <ul class="list list--square" style="margin-top:10px">
        <li>Special rates at Brellwick Inns</li>
        <li>Discount on fares from Trelo Trains</li>
        <li>Discounts on home and auto insurance thought the Halvesta Group and Prudora Choice</li>
        <li>Special rates on medical and dental insurance through Bluefen Cover Canada</li>
        <li>Special rates with Kestrin Mobile or Vomba</li>
        <li>Discounts on tickets from Olstander Stageworks</li>
        <li>Discounts on tickets from Marquee Tours Nationwide</li>
      </ul>
    </section>

    <section class="section" style="top:706px">
      <span class="pill">ADVOCACY</span>
      <ul class="list list--tick" style="margin-top:8px">
        <li><svg><use href="#tick"/></svg>NGAD advocates on behalf of you and your patients</li>
        <li><svg><use href="#tick"/></svg>We support the development of the specialty of emergency medicine for you</li>
        <li><svg><use href="#tick"/></svg>Gain a larger voice representing you and your specialty</li>
      </ul>
    </section>

    <section class="section" style="top:877px">
      <span class="pill">NETWORKING OPPORTUNITIES</span>
      <ul class="list list--tick" style="margin-top:8px">
        <li><svg><use href="#tick"/></svg>Opportunity to become involved with NGAD committees and sections</li>
        <li><svg><use href="#tick"/></svg>Connect with colleagues and potential mentors at events and through online discussions</li>
      </ul>
    </section>
  </div>

  <footer class="members">
    <span>MEMBER TYPES</span><span class="members__sep"></span>
    <span>PHYSICIAN MEMBERS</span><span class="members__sep"></span>
    <span>RESIDENT MEMBERS</span><span class="members__sep"></span>
    <span>STUDENT MEMBERS</span><span class="members__sep"></span>
    <span>ASSOCIATE MEMBERS</span>
  </footer>
</main>
</body>
</html>
```